Tallow Salmon Labels

We need a graphic design label for a new product launch. Tallow is an 100% Australian family business specialised in making marinades made from natural and locally sourced fresh ingredients for fish and seafood. We make remarkable food for fine cooking prepared by hand at our kitchen in Marlow Heath, using the same ingredients and techniques you would use at home.

We are planning to launch three marinades for salmon.
The flavours are:

- Herb, Lemon & Cracked Black Pepper
- Ginger, Honey & Soy
- Coriander, Lemongrass, Shallot and Ginger

The marinades will be packed in a 300 grams clear pouch with spout and sold in the seafood section of a major retail supermarket.

Measurements of the pouch: 140 mm wide and 210 mm high but only 160 mm high from the spout downwards.

Label: For the label, It will be a 120mm wide X 120mm high If not slightly smaller. Please refer to File 2: to see the pouch.

The label will cover 75% of the front of the pouch and the marinade itself will be visible in the remaining 25 % of the pouch. The colours of the marinades are green for Herb, Lemon & Cracked Black Pepper and Coriander, Lemongrass, Shallot and Ginger; and dark brown for Ginger, Honey & Soy.

Our marinades do not contain additives. The marinades are Gluten free.

The label needs to visually communicate that the marinade is used for salmon.

Please choose a suitable typography for our name Tallow that communicates an artisan feel.

Please refer to File 1 as a guide to what we would like, but keep in mind we are very open to any ideas you may have.

Colours should reflect the nature of our business, as outlined above.
Updates

Hello Designers,

This is what the actual pouch looks like https://www.filecrate-example.net/sc/4kd9w2m7x1/Qa81Lpt3z_

We would like the label to be roughly 120mm X 120mm or within those parameters to fit the packaging.

Thank you!
- Moira

Hey Designers,

we have been looking at your designs and while we have liked some elements of them we would like to see more creativity with the actual graphics and shapes of the labels, different colour contrast and more clever and quirky designs. We want to make fish fun and interesting to consumers, something rustic that catches the eye but at the same time is still sophisticated and upmarket. 

We would like to see the following on your packaging designs:

- Pastels colours (green, blue and yellow).
- The 'Tallow gourmet' font to be in bolder typography
- An ink looking stamp for 'gluten free, no additives'
- Something about the product being hand crafted
- Must include the following text: Marinades made from natural and locally sourced fresh ingredients for fish and seafood

here are some examples for you to be inspired by

Some font ideas ..

http://pinboardly-example.net/pin/518203947716250341/
http://pinboardly-example.net/pin/73915268401837762/
http://pinboardly-example.net/pin/629450183027741856/
http://pinboardly-example.net/pin/384720615099214730/
http://pinboardly-example.net/pin/957301846620387412/
http://pinboardly-example.net/pin/140862397785023561/

colours/images/graphics

http://pinboardly-example.net/pin/803174529936610248/
http://pinboardly-example.net/pin/471028395512846307/
http://pinboardly-example.net/pin/695283017740158236/
http://pinboardly-example.net/pin/332610847958271649/ (We like this concept) 

Good luck! 

 

Target Market(s)

Home cooks, young professionals, anyone with a healthy eating lifestyle.

Industry/Entity Type

Graphic Design

Requirements
Must have
• The label needs to visually communicate that the marinade is used for salmon.
- Include "Gluten Free" and "No Additives" on the label
- Outline the freshness of the ingredients used in the marinade eg. Coriander, Lemongrass, Shallot and Ginger to be included on the label.
- Bright and eye catching colours (food friendly colours).
Nice to have
• - Open to pastel colours
- Vector drawings
Should not have
• - dull colours

```html
<!DOCTYPE html>
<html lang="en">
<head>
<meta charset="utf-8">
<title>Tallow – Herb, Lemon &amp; Cracked Black Pepper Label</title>
<link rel="stylesheet" href="https://fonts.googleapis.com/css2?family=Cinzel:wght@400;600&family=Libre+Baskerville:wght@400;700&family=Open+Sans:wdth,wght@75,700;75,800;100,400&display=swap">
<style>
  :root {
    --salmon: #f26b3a;
    --salmon-light: #f8895a;
    --pepper-dark: #2a2528;
    --pepper-mid: #4a4245;
    --herb-dark: #5b6a2c;
    --herb-light: #a9ad6a;
    --lemon: #f6c51c;
    --lemon-light: #fbe07a;
    --band-green: #8fbf5f;
    --accent-orange: #f15a22;
    --ink: #1f1f1f;
    --rule: #3a3a3a;
    --paper: #ffffff;
  }
  * { margin: 0; padding: 0; box-sizing: border-box; }
  html, body { width: 1200px; height: 1196px; overflow: hidden; background: var(--paper); }
  .label { position: relative; width: 1200px; height: 1196px; overflow: hidden; }

  .photo { position: absolute; }
  .photo--salmon { left: 0; top: 0; width: 395px; height: 598px;
    background: linear-gradient(160deg, var(--salmon-light), var(--salmon) 60%, #e55a2a); }
  .photo--herbs { left: 0; top: 598px; width: 395px; height: 598px;
    background: linear-gradient(200deg, var(--herb-light), var(--herb-dark)); }
  .photo--pepper { left: 811px; top: 0; width: 389px; height: 598px;
    background: radial-gradient(circle at 60% 40%, var(--pepper-mid), var(--pepper-dark)); }
  .photo--lemons { left: 811px; top: 598px; width: 389px; height: 598px;
    background: radial-gradient(circle at 70% 60%, var(--lemon-light), var(--lemon) 70%); }

  .center-band { position: absolute; left: 395px; top: 0; width: 416px; height: 1196px;
    background: var(--band-green);
    border-left: 3px solid var(--accent-orange); border-right: 3px solid var(--accent-orange); }

  .brand { position: absolute; left: 472px; top: 66px; width: 260px; height: 83px;
    border-top: 2px solid var(--paper); border-bottom: 2px solid var(--paper);
    display: flex; align-items: center; justify-content: center;
    font-family: "Cinzel", serif; font-weight: 600; font-size: 50px; color: var(--paper);
    letter-spacing: 0; }

  .net-weight { position: absolute; left: 395px; width: 416px; top: 1102px; text-align: center;
    font-family: "Open Sans", sans-serif; font-size: 34px; color: var(--paper); }

  .frame { position: absolute; left: 0; top: 0; }

  .stars { position: absolute; left: 326px; width: 551px; display: flex; justify-content: space-between;
    color: var(--accent-orange); font-size: 17px; line-height: 1; }
  .stars--top { top: 376px; }
  .stars--bottom { top: 806px; }

  .rule { position: absolute; left: 326px; width: 551px; height: 2px; background: var(--rule); }

  .headline { position: absolute; left: 348px; top: 410px; }
  .headline__amp { font-family: "Libre Baskerville", serif; font-weight: 700; fill: var(--band-green); }
  .headline__line { font-family: "Open Sans", sans-serif; font-stretch: 75%; font-weight: 800; fill: var(--ink); }

  .tagline { position: absolute; left: 326px; width: 551px; top: 606px; text-align: center;
    font-family: "Libre Baskerville", serif; font-size: 13.5px; line-height: 20px; color: var(--ink);
    text-transform: uppercase; white-space: nowrap; }

  .ribbon { position: absolute; left: 348px; top: 664px; }
  .ribbon__shape { fill: var(--accent-orange); }
  .ribbon__place { font-family: "Open Sans", sans-serif; font-stretch: 75%; font-weight: 800; fill: var(--ink); }
  .ribbon__lead { position: absolute; left: 368px; top: 671px; width: 168px; text-align: center;
    font-family: "Libre Baskerville", serif; font-size: 16px; line-height: 21px; color: var(--paper); white-space: nowrap; }

  .claims { position: absolute; left: 326px; width: 551px; top: 760px; text-align: center;
    font-family: "Libre Baskerville", serif; font-size: 22px; color: var(--ink); white-space: nowrap; }
</style>
</head>
<body>
<main class="label">
  <div class="photo photo--salmon" role="img" aria-label="Close-up of raw salmon fillet"></div>
  <div class="photo photo--herbs" role="img" aria-label="Dried green herbs"></div>
  <div class="photo photo--pepper" role="img" aria-label="Whole black peppercorns"></div>
  <div class="photo photo--lemons" role="img" aria-label="Fresh lemons, one cut in half"></div>

  <div class="center-band"></div>
  <div class="brand">TALLOW</div>
  <div class="net-weight">300 gr</div>

  <svg class="frame" width="1200" height="1196" viewBox="0 0 1200 1196" aria-hidden="true">
    <defs>
      <path id="frame-shape" d="M 210 280 L 470 280 Q 540 280 560 262 Q 601 240 643 262 Q 663 280 733 280 L 993 280 A 50 50 0 0 0 1043 330 L 1043 880 A 50 50 0 0 0 993 930 L 733 930 Q 663 930 643 948 Q 601 970 560 948 Q 540 930 470 930 L 210 930 A 50 50 0 0 0 160 880 L 160 330 A 50 50 0 0 0 210 280 Z"/>
    </defs>
    <use href="#frame-shape" fill="#ffffff"/>
    <use href="#frame-shape" fill="none" stroke="#f15a22" stroke-width="5" transform="translate(601.5 605) scale(0.975) translate(-601.5 -605)"/>
    <use href="#frame-shape" fill="#ffffff" transform="translate(601.5 605) scale(0.96) translate(-601.5 -605)"/>
  </svg>

  <div class="stars stars--top" aria-hidden="true">
    <span>★</span><span>★</span><span>★</span><span>★</span><span>★</span><span>★</span><span>★</span><span>★</span><span>★</span><span>★</span><span>★</span><span>★</span><span>★</span><span>★</span><span>★</span><span>★</span><span>★</span><span>★</span>
  </div>
  <div class="rule" style="top:404px"></div>

  <svg class="headline" width="530" height="185" viewBox="0 0 530 185">
    <text class="headline__amp" x="0" y="175" font-size="210" textLength="144" lengthAdjust="spacingAndGlyphs">&amp;</text>
    <text class="headline__line" x="157" y="55" font-size="62" textLength="359" lengthAdjust="spacingAndGlyphs">HERB, LEMON</text>
    <text class="headline__line" x="157" y="122" font-size="80" textLength="359" lengthAdjust="spacingAndGlyphs">CRACKED</text>
    <text class="headline__line" x="157" y="172" font-size="55" textLength="359" lengthAdjust="spacingAndGlyphs">BLACK PEPPER</text>
  </svg>

  <div class="rule" style="top:595px"></div>
  <p class="tagline">Marinades made from natural and locally<br>sourced fresh ingredients for fish and seafood</p>
  <div class="rule" style="top:651px"></div>

  <svg class="ribbon" width="529" height="60" viewBox="0 0 529 60">
    <polygon class="ribbon__shape" points="0,0 529,0 529,60 0,60 22,30"/>
    <text class="ribbon__place" x="210" y="47" font-size="46" textLength="294" lengthAdjust="spacingAndGlyphs">MARLOW HEATH</text>
  </svg>
  <p class="ribbon__lead">prepared by hand<br>at our kitchen in</p>

  <div class="rule" style="top:744px"></div>
  <p class="claims">CONTAINS NO ADDITIVES • GLUTEN FREE</p>
  <div class="rule" style="top:791px"></div>

  <div class="stars stars--bottom" aria-hidden="true">
    <span>★</span><span>★</span><span>★</span><span>★</span><span>★</span><span>★</span><span>★</span><span>★</span><span>★</span><span>★</span><span>★</span><span>★</span><span>★</span><span>★</span><span>★</span><span>★</span><span>★</span><span>★</span>
  </div>
</main>
</body>
</html>
```